Silverfern Hollow Counseling business cards

Dana Porvette, LCPC, NCC
(555)347-0816
www.silverfernhollowcounseling.example
dana@silverfernhollowcounseling.example

Business cards. I would like it on the same background as pictured. Not on a white business card. I have attached the logo that was done by another designer with artmarketly. I am open to looking at single-sided and double-sided designs.

Target Market(s)

teenagers and adults

Industry/Entity Type

mental health

Contact Information for Business Card

Dana Porvette, LCPC, NCC (555)347-0816 dana@silverfernhollowcounseling.example

Font styles to use
Other font styles liked:
• Cinzel

Colors

Designer to choose colors to be used in the design.

Requirements
Must have
• logo that is attached

```html
<!DOCTYPE html>
<html lang="en">
<head>
<meta charset="utf-8">
<title>Silverfern Hollow Counseling – Business Cards</title>
<link rel="stylesheet" href="https://fonts.googleapis.com/css2?family=Cinzel:wght@700&family=Montserrat:wght@600&family=Poppins:wght@400&display=swap">
<style>
  :root {
    --page: #ffffff;
    --teal: #3e7a8f;
    --silver: #b3b3b3;
    --coral: #e8806a;
    --card-white: #ffffff;
    --night-deep: #1d2831;
    --night-light: #4b5a64;
    --mist: #9fc0cf;
    --mark-tint: #dfe9ee;
  }
  * { margin: 0; padding: 0; box-sizing: border-box; }
  html, body {
    width: 1200px; height: 1200px; overflow: hidden;
    background: var(--page);
  }
  .sheet { position: relative; width: 1200px; height: 1200px; }
  .card {
    position: absolute; left: 200px; width: 796px; height: 463px;
    border-radius: 32px; overflow: hidden;
    box-shadow: 0 4px 14px rgba(0,0,0,0.28);
  }
  .card-front { top: 107px; background: var(--card-white); }
  .card-back  { top: 632px; }

  .front-wave { position: absolute; inset: 0; }
  .practice-name {
    position: absolute; left: 56px; top: 52px; width: 360px;
    text-align: center; color: var(--card-white);
    font-family: "Montserrat", sans-serif; font-weight: 600;
  }
  .practice-name .line-main { display: block; font-size: 29px; letter-spacing: -0.5px; }
  .practice-name .line-sub  { display: block; font-size: 23px; letter-spacing: 4px; margin-top: 4px; }

  .counselor {
    position: absolute; left: 50px; top: 336px;
  }
  .counselor-name {
    font-family: "Cinzel", serif; font-weight: 700; font-size: 22px;
    color: var(--teal); letter-spacing: 0.5px;
  }
  .contact-row {
    display: flex; align-items: center; gap: 8px; margin-top: 6px;
    font-family: "Poppins", sans-serif; font-size: 17px; color: var(--teal);
  }
  .contact-icon { width: 19px; height: 19px; flex: none; }

  .front-mark {
    position: absolute; left: 480px; top: 60px; width: 250px;
    display: flex; flex-direction: column; align-items: center; gap: 18px;
  }
  .mark-circle {
    width: 190px; height: 190px; border-radius: 50%; background: var(--mark-tint);
  }
  .mark-name {
    font-family: "Montserrat", sans-serif; font-weight: 600; font-size: 20px;
    color: var(--teal); letter-spacing: 0.5px;
  }

  .back-backdrop {
    position: absolute; inset: 0;
    background: radial-gradient(ellipse at 72% 18%, var(--night-light) 0%, #34424c 35%, var(--night-deep) 75%);
  }
  .back-mark {
    position: absolute; inset: 0;
    display: flex; flex-direction: column; align-items: center; justify-content: center;
    color: var(--mist);
    font-family: "Montserrat", sans-serif; font-weight: 600;
  }
  .back-circle {
    width: 150px; height: 150px; border-radius: 50%; background: var(--mist);
    margin-bottom: 38px;
  }
  .back-mark .line-main { font-size: 36px; letter-spacing: -0.5px; }
  .back-mark .line-sub  { font-size: 26px; letter-spacing: 5px; margin-top: 6px; }
</style>
</head>
<body>
<main class="sheet">
  <section class="card card-front" aria-label="Business card front">
    <svg class="front-wave" viewBox="0 0 796 463" preserveAspectRatio="none" aria-hidden="true">
      <path d="M0 355 C 80 230, 220 200, 340 180 C 450 160, 500 90, 511 0 L 506 0 C 470 110, 380 160, 280 175 C 150 195, 60 225, 0 268 Z" fill="var(--silver)"/>
      <path d="M0 0 L506 0 C 470 110, 380 160, 280 175 C 150 195, 60 225, 0 268 Z" fill="var(--teal)"/>
    </svg>

    <h1 class="practice-name">
      <span class="line-main">SILVERFERN HOLLOW</span>
      <span class="line-sub">COUNSELING</span>
    </h1>

    <div class="front-mark">
      <div class="mark-circle"></div>
      <div class="mark-name">Silverfern Hollow</div>
    </div>

    <div class="counselor">
      <p class="counselor-name">DANA PORVETTE, LCPC, NCC</p>
      <p class="contact-row">
        <svg class="contact-icon" viewBox="0 0 20 20" aria-hidden="true">
          <circle cx="10" cy="10" r="10" fill="var(--coral)"/>
          <path d="M6.5 5.2 L8.3 5 L9.2 7.4 L8 8.3 C8.6 9.7 9.9 11 11.5 11.8 L12.4 10.7 L14.8 11.6 L14.6 13.4 C10.2 13.7 6.2 9.6 6.5 5.2 Z" fill="#fff"/>
        </svg>
        (555)347-0816
      </p>
      <p class="contact-row">
        <svg class="contact-icon" viewBox="0 0 20 20" aria-hidden="true">
          <circle cx="10" cy="10" r="10" fill="var(--coral)"/>
          <rect x="5" y="6.5" width="10" height="7" fill="#fff"/>
          <path d="M5 6.5 L10 10.5 L15 6.5" fill="none" stroke="var(--coral)" stroke-width="1"/>
        </svg>
        dana@silverfernhollowcounseling.example
      </p>
    </div>
  </section>

  <section class="card card-back" aria-label="Business card back">
    <div class="back-backdrop" role="img" aria-label="Dim, softly lit office interior backdrop in slate blue tones"></div>
    <div class="back-mark">
      <div class="back-circle"></div>
      <span class="line-main">SILVERFERN HOLLOW</span>
      <span class="line-sub">COUNSELING</span>
    </div>
  </section>
</main>
</body>
</html>
```